ONE PAGE WEB DESIGN NEEDED for Finance Company

We need a web design (ONE PAGE DESIGN ONLY) for a new finance website called Brightwell Lending. Brightwell Lending helps customers get the right loan, whether its a home loan, investment loan, business loan etc.

You are required to come up with just the homepage design. Professionalism and quality is the key factors in the successful design.

Here are a few design questions to help you out:

-
What information should be used on the page?
Ive provided a document which outlines all the information needed to put on homepage (attached to the brief - called brightwell_page_info). Also see the Must Have section below on this brief.

-
What links should appear in the navigation/footer?:
The navigation should provide links to the following pages (NOTE: services link has subcategories):
1 Homepage
2 Services
- Home loans
- Investment loans
- Refinancing loans
- Business loans
3 About Us
4 FAQ
5 Contact Us

-
What colors should be used in the design?
Our company colors - Cyan: #2EADE3, Blue: #004B70, White. Feel free to submit designs with slight variations if you feel it improves the design.

-
What should the layout of the page be?
This is up to you to come up with - we are open to different layouts for the page design (as long as they capture the information effectively and making it easy to understand).

Target Market(s)

Potential Home owners, Families and Business Owners

Industry/Entity Type

Business

Requirements
Must have
• - Must contain our logo (attached as PNG and Illustrator file)
- Winning designer must supply a Photoshop file (PSD) that will allow us.
Nice to have
• - Should include photos/images of families, professional groups, tradespeople etc (you can use stock photos from PixQuarry and I will purchase them once you are selected as the winning design)
- Link to a loan calculator somewhere on front page with a button 'Find out how much you could borrow' (or maybe even try adding a loan calculator to the homepage if you think this would look good)
- Page should have a main headline "Finding the right loan for you" or "Brightwell Lending finds the right loan for our customers."
- Must include Accreditation logos somewhere on the homepage (will try and supply these soon)
Should not have
• - Poor quality designs will not be considered
- Do not use clipart

```html
<!DOCTYPE html>
<html lang="en">
<head>
<meta charset="utf-8">
<title>Brightwell Lending – Home</title>
<link rel="stylesheet" href="https://fonts.googleapis.com/css2?family=Ubuntu:wght@400;500;700&family=Arimo:wght@400&display=swap">
<style>
:root{
  --cyan:#1fb0e3;
  --cyan-dark:#1595c6;
  --blue:#004b70;
  --ink:#3a3a3a;
  --body:#2c2c2c;
  --card-head:#333333;
  --footer:#e6e6e6;
  --badge:#d3d5da;
}
*{box-sizing:border-box;margin:0;padding:0}
html,body{width:1200px;height:1157px;overflow:hidden}
body{position:relative;background:linear-gradient(#f0f0f0,#fafafa 40%,#f2f2f2);font-family:"Ubuntu",sans-serif;color:var(--ink)}
.top-rule{position:absolute;left:0;top:6px;width:1200px;height:3px;background:#e3e3e3}
.abs{position:absolute}

.brand{left:0;width:1200px;top:30px;display:flex;flex-direction:column;align-items:center;gap:12px}
.brand-mark{width:52px;height:52px;border-radius:50%;background:var(--cyan)}
.brand-name{font-size:27px;font-weight:500;color:var(--cyan);letter-spacing:-.3px}

.search{left:840px;top:27px;width:125px;height:21px;border:1px solid #ddd;background:#fff;font:11px "Arimo",sans-serif;color:#bbb;padding:4px 6px}
.search-go{left:969px;top:27px;width:31px;height:20px;border-radius:3px;background:linear-gradient(#2a97d0,#0d6aa3);color:#fff;font-size:13px;text-align:center;line-height:20px}

.main-nav{left:193px;top:133px;width:816px;height:30px;border-radius:3px;background:linear-gradient(#3bbdec,#17a6dc);display:flex}
.main-nav a{display:block;height:30px;line-height:30px;text-align:center;font-size:10.5px;font-weight:700;color:#fff;text-decoration:none;border-right:1px solid #55c6ee}
.main-nav a:last-child{border-right:none}
.main-nav a.current{color:var(--blue)}

.hero{left:193px;top:176px;width:816px;height:188px;border:1px solid #ddd;background:#fff;border-radius:2px;overflow:hidden}
.service-menu{position:absolute;left:0;top:0;width:226px;height:186px;background:linear-gradient(#fff,#f1f1f1);border-right:1px solid #e0e0e0;list-style:none;padding:28px 0 0 20px}
.service-menu li{width:189px;height:34.5px;line-height:31px;font-size:15.5px;color:#333;padding-left:22px;position:relative;border-bottom:1px dotted #9a9a9a}
.service-menu li:last-child{border-bottom:none}
.bullet{position:absolute;width:9px;height:9px;border-radius:50%;background:var(--cyan)}
.bullet::after{content:"";position:absolute;left:3px;top:2.5px;border-left:4px solid #fff;border-top:2px solid transparent;border-bottom:2px solid transparent}
.service-menu .bullet{left:3px;top:12px}
.hero-photo{position:absolute;left:227px;top:0;width:588px;height:186px;background:radial-gradient(ellipse 240px 150px at 300px 110px,#b7aaa0,#d9d4d0 55%,#fff 85%)}
.hero-call{position:absolute;left:510px;top:151px;width:304px;height:35px;background:#f3f3f3;border-top-left-radius:6px;font-size:17px;line-height:36px;padding-left:24px;color:#444}
.hero-call span{color:var(--cyan)}

.headline{left:212px;top:393px;font-size:26px;font-weight:400;color:#444}
.headline span{color:var(--cyan)}
.intro{left:212px;width:790px;font-family:"Arimo",sans-serif;font-size:12.6px;line-height:25.7px;color:var(--body)}
.divider{left:212px;top:612px;width:776px;height:2px;background:linear-gradient(90deg,rgba(31,176,227,0),var(--cyan) 25%,var(--cyan) 75%,rgba(31,176,227,0))}

.approach{left:214px;top:652px;font-size:19.5px;color:#444}
.borrow-btn{left:762px;top:632px;width:223px;height:67px;border:1px solid #bcd6e4;border-radius:5px;background:linear-gradient(#fff,#eef5f9);box-shadow:0 2px 3px rgba(0,0,0,.15)}
.borrow-icon{position:absolute;left:12px;top:9px;width:38px;height:48px;border-radius:4px;background:linear-gradient(#5a6b80,#3a8b4a)}
.borrow-text{position:absolute;left:58px;top:15px;width:160px;text-align:center;font-size:16.5px;line-height:19px;color:var(--cyan-dark)}

.loan-card{top:718px;width:186px;height:207px;border:1px solid #d6d6d6;border-radius:3px;background:linear-gradient(#fff 60%,#efefef)}
.loan-card h2{height:32px;margin:-1px -1px 0;background:var(--card-head);border-radius:3px 3px 0 0;font-size:16.5px;font-weight:400;color:#fff;line-height:33px;padding-left:16px}
.loan-card h2 b{color:var(--cyan);font-weight:700}
.loan-card ul{list-style:none;margin:30px 0 0 16px;width:152px}
.loan-card li{position:relative;font-size:11px;line-height:25.7px;color:#333;padding-left:14px;border-bottom:1px dotted #8e8e8e;white-space:nowrap}
.loan-card li.cont{border-bottom:none}
.loan-card li .bullet{left:0;top:8px;width:8px;height:8px}
.loan-card li .bullet::after{left:2.5px;top:2px;border-left-width:3.5px}
.loan-card .plain{font-size:11px;color:#333;margin:31px 0 0 16px;line-height:25.7px}
.loan-card .plain + ul{margin-top:0}

.footer{left:0;top:975px;width:1200px;height:182px;background:var(--footer);border-top:2px solid #d8d8d8}
.footer-links{position:absolute;top:12px;left:0;width:1200px;text-align:center;font-size:8.8px;color:#333;word-spacing:1px}
.footer-links i{font-style:normal;margin:0 4px}
.contact{position:absolute;left:298px;top:75px;font-size:11.5px;color:#444}
.contact .phone{display:flex;align-items:center;gap:8px;font-size:26px;color:var(--cyan);line-height:28px;margin:2px 0 0}
.contact .phone svg{flex:none}
.badge{position:absolute;background:var(--badge);border-radius:4px}
.copyright{position:absolute;top:165px;left:0;width:1200px;text-align:center;font-size:10px;color:#333}
</style>
</head>
<body>
<div class="top-rule"></div>

<header class="abs brand">
  <div class="brand-mark"></div>
  <div class="brand-name">Brightwell Lending</div>
</header>
<div class="abs search">Search here</div>
<div class="abs search-go">GO</div>

<nav class="abs main-nav">
  <a class="current" href="#" style="width:170px">HOME PAGE</a>
  <a href="#" style="width:168px">SERVICES</a>
  <a href="#" style="width:160px">ABOUT US</a>
  <a href="#" style="width:153px">FAQ</a>
  <a href="#" style="width:165px">CONTACT US</a>
</nav>

<section class="abs hero">
  <ul class="service-menu">
    <li><span class="bullet"></span>Home loans</li>
    <li><span class="bullet"></span>Investment loans</li>
    <li><span class="bullet"></span>Refinancing loans</li>
    <li><span class="bullet"></span>Business loans</li>
  </ul>
  <div class="hero-photo" role="img" aria-label="Stock photo of a smiling group of business professionals"></div>
  <div class="hero-call">Call Us To Know More <span>1800 555 019</span></div>
</section>

<h1 class="abs headline"><span>Brightwell Lending</span> finds the right loan for our customers.</h1>
<p class="abs intro" style="top:441px">At Brightwell Lending we work hard to find the right loan for our customers.&nbsp; We do that because we are backed by sound industry knowledge, professional experience and a great customer service approach.</p>
<p class="abs intro" style="top:518px">Brightwell Lending guarantees that we will always tailor the best solution for your individual lending needs. We can do that because we have access to a wide variety of lending options from major banks to non-bank lenders and we are committed to finding the right lending product for you.</p>
<div class="abs divider"></div>

<p class="abs approach">We offer a unique approach to help you find the right:</p>
<a class="abs borrow-btn" href="#">
  <span class="borrow-icon" role="img" aria-label="Illustration of a businessman with money"></span>
  <span class="borrow-text">Find out how much you could borrow</span>
</a>

<section class="abs loan-card" style="left:213px">
  <h2><b>Home</b> loans</h2>
  <ul>
    <li><span class="bullet"></span>Home buyers</li>
    <li><span class="bullet"></span>First home buyers</li>
    <li><span class="bullet"></span>Over 20 lenders</li>
  </ul>
</section>
<section class="abs loan-card" style="left:409px">
  <h2><b>Investment</b> loans</h2>
  <ul>
    <li><span class="bullet"></span>Property investment loans</li>
    <li><span class="bullet"></span>Interest only loans</li>
  </ul>
</section>
<section class="abs loan-card" style="left:604px">
  <h2><b>Refinancing</b> loans</h2>
  <ul>
    <li class="cont"><span class="bullet"></span>Refinancing for the best</li>
    <li>rate</li>
    <li><span class="bullet"></span>Upsizing or downsizing</li>
    <li class="cont"><span class="bullet"></span>Change from a variable</li>
    <li>to a fixed rate</li>
  </ul>
</section>
<section class="abs loan-card" style="left:800px">
  <h2><b>Business</b> loans</h2>
  <p class="plain">Business Finance</p>
  <ul>
    <li><span class="bullet"></span>Long term</li>
    <li><span class="bullet"></span>Short term</li>
    <li><span class="bullet"></span>Equipment and</li>
    <li><span class="bullet"></span>Leasing</li>
  </ul>
</section>

<footer class="abs footer">
  <div class="footer-links">HOME<i>|</i>ABOUT US<i>|</i>SERVICES<i>|</i>FAQ<i>|</i>CAREERS<i>|</i>PRIVACY POLICY<i>|</i>SITEMAP<i>|</i>CONTACT US</div>
  <div class="contact">
    <div>Contact Brightwell Lending today on:</div>
    <div class="phone">
      <svg width="26" height="26" viewBox="0 0 26 26"><circle cx="13" cy="13" r="13" fill="#1fb0e3"/><path d="M9 6c1 0 2 3 2 4s-1.5 1.5-1 3 2.5 4 4 4.5 2-1 3-1 3 1 3 2-1.5 2.5-3 2.5C12 21 6 14 6 9c0-1.5 2-3 3-3z" fill="#fff"/></svg>
      1800 555 019
    </div>
    <div>to find out more.</div>
  </div>
  <div class="badge" style="left:512px;top:58px;width:74px;height:64px" role="img" aria-label="Accreditation badge"></div>
  <div class="badge" style="left:617px;top:68px;width:160px;height:57px" role="img" aria-label="Accreditation badge"></div>
  <div class="badge" style="left:808px;top:57px;width:76px;height:76px" role="img" aria-label="Accreditation badge"></div>
  <div class="copyright">Copyright © Brightwell Lending</div>
</footer>
</body>
</html>
```